Custom Label for Essential Oils Bottle

We are a brand new company who specializes in seeking 100% pure essential oils. You would need to create a label that is similar to the designs attached, but unique to us. Our favorite label design is by quiet harbor blends. We really like how elegant their look is and would like to model that.
We will give the exact text of what we need put into the label to the winner after our favorite design is selected. Also, our logo is attached.
We would like the whole line to follow the same design with minor or tweaks for each scent (different color and text is all).
The label size would be 3" x 1.125" . There will be approximately 60 different oils in our first line but we only need 6 created for our first run.
Attached are the logo designs we really like.
Our first scent will be for a "Lemon" Essential oil bottle so design accordingly. The additional scents will be clove bud , peppermint, sweet orange, rosemary, and eucalyptus.
Thanks so much, and I look forward to seeing your designs!
Tom
Women, ages 18-65, wealthy
It Company

```html
<!DOCTYPE html>
<html lang="en">
<head>
<meta charset="UTF-8">
<title>Lumen Grove – Lemon Essential Oil Label</title>
<link href="https://fonts.googleapis.com/css2?family=Open+Sans:wght@400;700&family=Libre+Baskerville:ital@1&display=swap" rel="stylesheet">
<style>
  :root {
    --page-bg: #f3f3f5;
    --label-yellow: #fdd10a;
    --panel-black: #050505;
    --ink-black: #0a0a0a;
    --text-white: #ffffff;
    --ornament-grey: #cfcfcf;
  }
  html, body {
    margin: 0;
    padding: 0;
    width: 835px;
    height: 1200px;
    overflow: hidden;
    background: var(--page-bg);
  }
  .canvas {
    position: relative;
    width: 835px;
    height: 1200px;
  }
  .label {
    position: absolute;
    left: 97px;
    top: 180px;
    width: 640px;
    height: 840px;
    background: var(--label-yellow);
    overflow: hidden;
  }
  .brand {
    position: absolute;
    left: 0;
    right: 0;
    top: 92px;
    text-align: center;
    font-family: "Open Sans", sans-serif;
    font-weight: 700;
    font-size: 64px;
    line-height: 1.1;
    color: var(--ink-black);
    letter-spacing: 1px;
  }
  .scent-panel {
    position: absolute;
    left: 20px;
    right: 0;
    top: 272px;
    height: 525px;
    background: var(--panel-black);
    border-top-left-radius: 80px;
  }
  .scent-name {
    position: absolute;
    left: 0;
    right: 20px;
    top: 68px;
    text-align: center;
    font-family: "Open Sans", sans-serif;
    font-weight: 700;
    font-size: 76px;
    line-height: 1;
    color: var(--text-white);
    margin: 0;
  }
  .botanical-name {
    position: absolute;
    left: 0;
    right: 20px;
    top: 160px;
    text-align: center;
    font-family: "Libre Baskerville", serif;
    font-style: italic;
    font-size: 40px;
    line-height: 1;
    color: var(--label-yellow);
    margin: 0;
  }
  .floral-ornament {
    position: absolute;
    left: 133px;
    top: 298px;
    width: 125px;
    height: 180px;
    border-radius: 40px 40px 20px 20px;
    background: radial-gradient(circle at 50% 50%, var(--ornament-grey) 0%, #6b6b6b 55%, var(--panel-black) 100%);
  }
  .purity-note {
    position: absolute;
    left: 305px;
    top: 400px;
    font-family: "Open Sans", sans-serif;
    font-weight: 400;
    font-size: 26px;
    line-height: 1.25;
    color: var(--text-white);
    margin: 0;
  }
  .volume {
    position: absolute;
    right: 30px;
    top: 432px;
    font-family: "Open Sans", sans-serif;
    font-weight: 700;
    font-size: 22px;
    color: var(--text-white);
    letter-spacing: 1px;
    margin: 0;
  }
</style>
</head>
<body>
<main class="canvas">
  <section class="label">
    <div class="brand">Lumen<br>Grove</div>
    <div class="scent-panel">
      <h1 class="scent-name">LEMON</h1>
      <p class="botanical-name">Cirtus Lemon</p>
      <div class="floral-ornament" role="img" aria-label="White swirling floral ornament with leaves and small flowers"></div>
      <p class="purity-note">100% Pure<br>Essential Oil</p>
      <p class="volume">(15ml)</p>
    </div>
  </section>
</main>
</body>
</html>
```